Aviation Banner Ad Designs

SkyLedgerMetrics provides access to the most accurate aircraft operating cost information, to compare Piston, Turboprop and Jet aircraft.

The banners ads will be used for retargeting/remarketing - to bring visitors back to the site. The banners should remind and reinforce the key messages of what the site provides.

Target Market(s)

Private aircraft buyers including:
- Aircraft Brokers
- Charter Operators
- Corporate Flight Departments
- Aircraft Management companies
- Financial Institutions
- Aircraft Owners
- Prospective Buyers

Requirements
Must have
• A. Banner Objective
The visual and textual content of the banner should remind the viewer about the features of the site, and prompt them to return to the site.
1. Arresting visual
2. Headline
3. Single message
4. Compelling CTA
5. Logo - big enough to see
6. Standard DWR ad sizes/specs

B. Design Elements
Logo: As attached
Main Title: Calculate Jet Operating Costs
Subtitle: Compare Ownership Usage Scenarios
Call to Action Button: Compare Ownership Costs
Background: Several images supplied as options

C. Banner Sizes
Do examples as 300×250 , 728×90 , 160×600
Final sizes to also include 320×100 , 336x280 , 300x600

Finally delivery as .jpg files.

Font - use same font as on site

```html
<!DOCTYPE html>
<html lang="en">
<head>
<meta charset="utf-8">
<title>SkyLedgerMetrics – Banner Set</title>
<link rel="stylesheet" href="https://fonts.googleapis.com/css2?family=Montserrat:wght@400;500;700&display=swap">
<style>
  :root {
    --board-top: #f7f8fa;
    --board-bottom: #ededed;
    --navy: #0c2444;
    --red: #d62029;
    --white: #ffffff;
    --ink: #111418;
    --sky-cloud: #eef3f8;
    --sky-haze: #c3d5e6;
    --sky-mid: #7fa3c6;
    --sky-deep: #3f6f9c;
  }
  * { margin: 0; padding: 0; box-sizing: border-box; }
  html, body { width: 1200px; height: 1032px; overflow: hidden; }
  body {
    position: relative;
    font-family: "Montserrat", Arial, sans-serif;
    background: linear-gradient(180deg, var(--board-top) 0%, var(--board-bottom) 100%);
  }
  .backdrop-aircraft {
    position: absolute; left: 583px; top: 146px; width: 549px; height: 239px;
    background: radial-gradient(ellipse at 50% 50%, rgba(255,255,255,0.9) 0%, rgba(255,255,255,0.35) 55%, rgba(255,255,255,0) 75%);
  }
  .banner {
    position: absolute; overflow: hidden; background: var(--white);
    box-shadow: 0 6px 14px rgba(0,0,0,0.22);
  }
  .banner svg.banner-art { position: absolute; inset: 0; }
  .brand {
    position: absolute; display: flex; align-items: center;
    color: var(--ink); font-weight: 700; letter-spacing: 0.2px; white-space: nowrap;
  }
  .brand-square { background: var(--red); flex: none; }
  .headline {
    position: absolute; color: var(--white); font-weight: 700; text-transform: uppercase;
    line-height: 1.2; letter-spacing: 0.4px;
  }
  .subline {
    position: absolute; color: var(--white); font-weight: 400; line-height: 1.4;
  }
  .cta {
    position: absolute; display: flex; align-items: center; justify-content: center;
    background: var(--red); color: var(--white); border-radius: 999px;
    font-weight: 500; text-transform: uppercase; white-space: nowrap;
  }

  /* 160 x 600 skyscraper */
  .banner--skyscraper { left: 198px; top: 166px; width: 350px; height: 700px; }
  .banner--skyscraper .brand { left: 50px; top: 76px; font-size: 20px; gap: 10px; }
  .banner--skyscraper .brand-square { width: 24px; height: 24px; }
  .banner--skyscraper .headline { left: 0; right: 0; top: 452px; text-align: center; font-size: 30px; }
  .banner--skyscraper .subline { left: 0; right: 0; top: 537px; text-align: center; font-size: 21px; }
  .banner--skyscraper .cta { left: 62px; top: 613px; width: 222px; height: 52px; font-size: 12px; }

  /* 300 x 250 rectangle */
  .banner--rectangle { left: 609px; top: 457px; width: 392px; height: 327px; }
  .banner--rectangle .brand { left: 24px; top: 22px; font-size: 15px; gap: 7px; }
  .banner--rectangle .brand-square { width: 16px; height: 16px; }
  .banner--rectangle .headline { left: 26px; top: 264px; font-size: 17.5px; }
  .banner--rectangle .cta {
    left: 218px; top: 269px; width: 151px; height: 35px; padding: 0 10px;
    font-size: 7.5px; letter-spacing: 0;
  }

  /* standalone brand mark */
  .brand--showcase { left: 644px; top: 300px; font-size: 31px; gap: 12px; }
  .brand--showcase .brand-square { width: 34px; height: 34px; }
</style>
</head>
<body>
  <div class="backdrop-aircraft" role="img" aria-label="Faint airliner in flight, decorative backdrop"></div>

  <div class="brand brand--showcase"><span class="brand-square"></span>SkyLedgerMetrics</div>

  <section class="banner banner--skyscraper">
    <svg class="banner-art" width="350" height="700" viewBox="0 0 350 700">
      <defs>
        <linearGradient id="sky-tall" x1="0.2" y1="0" x2="0.5" y2="1">
          <stop offset="0" stop-color="var(--sky-deep)"/>
          <stop offset="0.35" stop-color="var(--sky-mid)"/>
          <stop offset="0.65" stop-color="var(--sky-haze)"/>
          <stop offset="1" stop-color="var(--sky-cloud)"/>
        </linearGradient>
        <radialGradient id="glow-tall" cx="0.55" cy="0.45" r="0.55">
          <stop offset="0" stop-color="#ffffff" stop-opacity="0.75"/>
          <stop offset="1" stop-color="#ffffff" stop-opacity="0"/>
        </radialGradient>
      </defs>
      <g role="img" aria-label="Photo of a twin-engine jet airliner banking above clouds">
        <polygon points="0,194 350,142 350,373 0,441" fill="url(#sky-tall)"/>
        <polygon points="0,194 350,142 350,373 0,441" fill="url(#glow-tall)"/>
      </g>
      <polygon points="0,184 350,132 350,142 0,194" fill="var(--red)"/>
      <polygon points="0,441 350,373 350,384 0,452" fill="var(--red)"/>
      <polygon points="0,452 350,384 350,700 0,700" fill="var(--navy)"/>
    </svg>
    <div class="brand"><span class="brand-square"></span>SkyLedgerMetrics</div>
    <h2 class="headline">Calculate Jet<br>Operating Costs</h2>
    <p class="subline">Compare Ownership<br>Usage Scenarios</p>
    <a class="cta">Compare Ownership Costs</a>
  </section>

  <section class="banner banner--rectangle">
    <svg class="banner-art" width="392" height="327" viewBox="0 0 392 327">
      <defs>
        <linearGradient id="sky-wide" x1="0.3" y1="0" x2="0.5" y2="1">
          <stop offset="0" stop-color="var(--sky-deep)"/>
          <stop offset="0.4" stop-color="var(--sky-mid)"/>
          <stop offset="0.7" stop-color="var(--sky-haze)"/>
          <stop offset="1" stop-color="var(--sky-cloud)"/>
        </linearGradient>
        <radialGradient id="glow-wide" cx="0.5" cy="0.5" r="0.55">
          <stop offset="0" stop-color="#ffffff" stop-opacity="0.7"/>
          <stop offset="1" stop-color="#ffffff" stop-opacity="0"/>
        </radialGradient>
      </defs>
      <g role="img" aria-label="Photo of a jet airliner climbing above clouds">
        <polygon points="0,99 392,41 392,198 0,249" fill="url(#sky-wide)"/>
        <polygon points="0,99 392,41 392,198 0,249" fill="url(#glow-wide)"/>
      </g>
      <polygon points="0,91 392,33 392,41 0,99" fill="var(--red)"/>
      <polygon points="0,249 392,198 392,207 0,258" fill="var(--red)"/>
      <polygon points="0,258 392,207 392,327 0,327" fill="var(--navy)"/>
    </svg>
    <div class="brand"><span class="brand-square"></span>SkyLedgerMetrics</div>
    <h2 class="headline">Calculate Jet<br>Operating Costs</h2>
    <a class="cta">Compare Ownership Costs</a>
  </section>
</body>
</html>
```